Powerpoint Presentation Template

Kindly design a business class Powepoint Presentation template for our business use. Please stick to our company colours or even pictures as shown on our website and Logo

```html
<!DOCTYPE html>
<html lang="en">
<head>
<meta charset="utf-8">
<title>Kelvora Properties – Presentation Template Slides</title>
<link href="https://fonts.googleapis.com/css2?family=Montserrat:wght@400;600;700&family=Open+Sans:wght@400;600&family=Titillium+Web:wght@600&display=swap" rel="stylesheet">
<style>
:root{
  --stage:#2e3a4d;
  --brick:#8e2b20;
  --brick-dark:#7a241a;
  --ink:#33393f;
  --muted:#8a8f94;
  --paper:#f8f8f8;
  --line:#d9d9d9;
  --slate:#8d9ba8;
  --teal:#4f7a72;
}
*{box-sizing:border-box;margin:0;padding:0}
html,body{width:1200px;height:1200px;overflow:hidden;background:var(--stage)}
body{position:relative;font-family:"Open Sans",sans-serif}
.page-brand{position:absolute;left:196px;top:16px;font-family:"Montserrat",sans-serif;font-weight:700;color:var(--brick);line-height:1}
.page-brand .name{font-size:40px;letter-spacing:-1px}
.page-brand .sub{font-size:27px;margin-left:30px;margin-top:2px}
.page-heading{position:absolute;left:646px;top:40px;font-family:"Titillium Web",sans-serif;font-weight:600;color:#fff;font-size:16.5px;line-height:20px}

.slide{position:absolute;width:277px;height:157px;background:var(--paper);overflow:hidden;box-shadow:0 2px 4px rgba(0,0,0,.35)}
.c1{left:131px}.c2{left:454px}.c3{left:778px}
.r1{top:113px}.r2{top:291px}.r3{top:474px}.r4{top:666px}.r5{top:844px}.r6{top:1027px}
.slide-title{position:absolute;left:10px;top:9px;font-family:"Montserrat",sans-serif;font-weight:700;font-size:7.2px;color:var(--brick);letter-spacing:.3px}
.slide-title::after{content:"";display:block;width:20px;height:1px;background:var(--brick);margin-top:3px}
.brand{position:absolute;right:11px;top:6px;font-family:"Montserrat",sans-serif;font-weight:700;color:var(--brick);font-size:8px;line-height:8px;text-align:right}
.brand small{display:block;font-size:6px}
.foot{position:absolute;left:0;right:0;bottom:0;height:8px;background:var(--brick);color:#fff;font-size:3px;display:flex;align-items:center;padding:0 8px;gap:4px}
.foot span:first-child{flex:1}
.foot b{font-weight:400;width:10px;text-align:right}
.tx{position:absolute;font-size:3.2px;line-height:5px;color:var(--muted)}
.tx.w{color:#e8e8e8}
.h{position:absolute;font-family:"Montserrat",sans-serif;font-weight:700;font-size:3.6px;color:var(--ink)}
.h.w{color:#fff}
.ph{position:absolute;border:1px solid #ddd}
.ph-build{background:linear-gradient(180deg,#a9bccd 0 38%,#a8744f 38% 70%,#7f6f5c 70%)}
.ph-site{background:linear-gradient(180deg,#b8c7d2 0 45%,#8a7d62 45% 75%,#6b6152 75%)}
.ph-glass{background:linear-gradient(180deg,#7e93a8 0 20%,#3d4a57 20% 80%,#6c6a62 80%)}
.ph-dusk{background:linear-gradient(180deg,#4a5d7a 0%,#6b5448 60%,#3a3230 100%)}
.ph-face{background:linear-gradient(180deg,#c9ccd0,#9da3aa)}
.chk{position:absolute;width:10px;height:10px;border-radius:50%;background:var(--brick)}
.chk::after{content:"";position:absolute;left:3px;top:2.3px;width:3.5px;height:2px;border-left:1.1px solid #fff;border-bottom:1.1px solid #fff;transform:rotate(-45deg)}
.chk.s{width:8px;height:8px}
.chk.s::after{left:2.3px;top:1.8px;width:3px;height:1.6px}
.cap{position:absolute;font-size:3.4px;font-weight:600;color:var(--ink);text-align:center}
.logo-card{position:absolute;background:#fff;border-radius:5px;font-family:"Montserrat",sans-serif;font-weight:700;color:var(--brick);text-align:center;line-height:1}
</style>
</head>
<body>

<div class="page-brand"><div class="name">KELVORA</div><div class="sub">Properties</div></div>
<div class="page-heading">Individual Slides - 01b<br>( Submission With Bigger Size - More Clarity)</div>

<!-- Row 1 -->
<section class="slide c1 r1">
  <h2 class="slide-title">PROPERTY DEVELOPMENT PROJECTS</h2>
  <div class="brand">KELVORA<small>Properties</small></div>
  <div class="cap" style="left:0;right:0;top:37px">Kelvora Estate Construction Project</div>
  <div class="ph ph-build" style="left:14px;top:54px;width:80px;height:40px" role="img" aria-label="Townhouse under construction"></div>
  <div class="ph ph-site" style="left:99px;top:54px;width:80px;height:40px" role="img" aria-label="Estate site with new houses"></div>
  <div class="ph ph-site" style="left:184px;top:54px;width:80px;height:40px" role="img" aria-label="Estate street view"></div>
  <div class="ph ph-build" style="left:14px;top:99px;width:80px;height:40px" role="img" aria-label="Finished brick townhouses"></div>
  <div class="ph ph-site" style="left:99px;top:99px;width:80px;height:40px" role="img" aria-label="Completed house exterior"></div>
  <footer class="foot"><span>Copyright © 2018 KELVORA PROPERTIES All rights reserved.</span><span>www.kelvoraprops.co.za</span><b>20</b></footer>
</section>

<section class="slide c2 r1">
  <div class="ph ph-build" style="left:0;top:0;width:277px;height:100px;border:0" role="img" aria-label="Brick townhouses with parked car"></div>
  <div class="logo-card" style="left:14px;top:12px;width:86px;height:40px;padding-top:8px;font-size:12px">KELVORA<div style="font-size:9px;margin-top:2px">Properties</div></div>
  <div style="position:absolute;left:0;top:100px;width:277px;height:57px;background:var(--brick)"></div>
  <div style="position:absolute;left:13px;top:116px;font-family:Montserrat,sans-serif;font-weight:700;font-size:13px;color:#fff">PROPERTY</div>
  <div style="position:absolute;left:13px;top:131px;font-family:Montserrat,sans-serif;font-size:7px;color:#f1d6d2;letter-spacing:.5px">DEVELOPMENT</div>
  <p class="tx w" style="left:100px;top:110px;width:168px">Kelvora Properties works in tandem with a partner group company in the development of real estate across the region. We are a multi faceted and well established property development company, acting as both owner and contractor in the specialised building of gated residential estates, rental apartment blocks, domestic complexes and business campuses.</p>
</section>

<section class="slide c3 r1">
  <h2 class="slide-title">ACCREDITATION &amp; AWARDS</h2>
  <div class="brand">KELVORA<small>Properties</small></div>
  <div style="position:absolute;left:8px;top:28px;width:261px;height:115px;border:1.5px solid #c9c9c9;border-radius:6px;background:#fff"></div>
  <svg style="position:absolute;left:8px;top:28px" width="261" height="115" viewBox="0 0 261 115" aria-hidden="true">
    <g fill="#d6d6d6">
      <rect x="12" y="12" width="24" height="20" rx="2"/><rect x="62" y="15" width="30" height="14" rx="2"/>
      <rect x="117" y="14" width="28" height="16" rx="2"/><rect x="170" y="14" width="34" height="16" rx="2"/>
      <rect x="222" y="14" width="34" height="16" rx="2"/>
    </g>
    <g fill="none" stroke="#8e2b20" stroke-width="1.4">
      <circle cx="24" cy="58" r="10"/><circle cx="77" cy="58" r="10"/><circle cx="131" cy="58" r="10"/>
      <circle cx="187" cy="58" r="10"/><circle cx="239" cy="58" r="10"/>
    </g>
    <g font-family="Montserrat,sans-serif" font-size="5.5" font-weight="700" fill="#8e2b20" text-anchor="middle">
      <text x="24" y="60">2003</text><text x="77" y="60">2007</text><text x="131" y="60">2008</text><text x="187" y="60">2008</text><text x="239" y="60">2009</text>
    </g>
    <g font-size="2.8" fill="#777" text-anchor="middle" font-family="Open Sans,sans-serif">
      <text x="24" y="76">Housing builder</text><text x="24" y="80">of the year</text><text x="24" y="84">regional award</text>
      <text x="77" y="76">Certificate for</text><text x="77" y="80">completed project</text><text x="77" y="84">public housing</text>
      <text x="131" y="76">Contractor of</text><text x="131" y="80">the year</text><text x="131" y="84">national award</text>
      <text x="187" y="76">Housing developer</text><text x="187" y="80">of the year</text><text x="187" y="84">regional award</text>
      <text x="239" y="76">Contractor of</text><text x="239" y="80">the year</text><text x="239" y="84">provincial award</text>
    </g>
  </svg>
  <footer class="foot"><span>Copyright © 2018 KELVORA PROPERTIES All rights reserved.</span><span>www.kelvoraprops.co.za</span><b>22</b></footer>
</section>

<!-- Row 2 -->
<section class="slide c1 r2">
  <h2 class="slide-title">OUR PORTFOLIO (FEATURED PROJECTS)</h2>
  <div class="brand">KELVORA<small>Properties</small></div>
  <div class="ph ph-glass" style="left:14px;top:33px;width:80px;height:40px" role="img" aria-label="Apartment block"></div>
  <div class="ph ph-glass" style="left:99px;top:33px;width:80px;height:40px" role="img" aria-label="College building"></div>
  <div class="ph ph-site" style="left:184px;top:33px;width:80px;height:40px" role="img" aria-label="Civic building construction"></div>
  <div class="cap" style="left:14px;width:80px;top:76px">Riverside Court</div>
  <div class="cap" style="left:99px;width:80px;top:76px">Northgate College</div>
  <div class="cap" style="left:184px;width:80px;top:76px">Lakeview Civic Building<br>Construction Project</div>
  <div class="ph ph-site" style="left:14px;top:89px;width:80px;height:40px" role="img" aria-label="Water treatment plant"></div>
  <div class="ph ph-build" style="left:99px;top:89px;width:80px;height:40px" role="img" aria-label="Estate townhouses"></div>
  <div class="ph ph-glass" style="left:184px;top:89px;width:80px;height:40px" role="img" aria-label="Transit station with bus"></div>
  <div class="cap" style="left:14px;width:80px;top:132px">Waste Water Treatment Plant<br>(Summit Mining)</div>
  <div class="cap" style="left:99px;width:80px;top:132px">Kelvora Estate</div>
  <div class="cap" style="left:184px;width:80px;top:132px">Metro Rapid Transit</div>
  <footer class="foot"><span>Copyright © 2018 KELVORA PROPERTIES All rights reserved.</span><span>www.kelvoraprops.co.za</span><b>23</b></footer>
</section>

<section class="slide c2 r2" style="background:var(--brick)">
  <div class="logo-card" style="left:20px;top:20px;width:90px;height:42px;padding-top:9px;font-size:12px">KELVORA<div style="font-size:9px;margin-top:2px">Properties</div></div>
  <div style="position:absolute;left:163px;top:100px;width:100px;text-align:center;font-family:Montserrat,sans-serif;font-weight:700;font-size:12px;color:#fff">TEMPLATE</div>
  <div style="position:absolute;left:163px;top:116px;width:100px;text-align:center;font-family:Montserrat,sans-serif;font-size:7px;color:#f1c9c3">SLIDE IDEAS</div>
</section>

<section class="slide c3 r2">
  <h2 class="slide-title">YOUR SLIDE TITLE HERE</h2>
  <div class="brand">KELVORA<small>Properties</small></div>
  <p class="tx" style="left:12px;top:32px;width:255px">Short sample text for this slide goes here. Replace it with a brief summary of the topic, the main idea and a clear statement for the audience to follow.</p>
  <div class="chk" style="left:30px;top:55px"></div><div class="h" style="left:49px;top:55px">YOUR TITLE HERE</div>
  <p class="tx" style="left:49px;top:61px;width:200px">Add a short description for this point here. Keep it clear and brief for the reader.</p>
  <div class="chk" style="left:30px;top:86px"></div><div class="h" style="left:49px;top:86px">YOUR TITLE HERE</div>
  <p class="tx" style="left:49px;top:92px;width:200px">Add a short description for this point here. Keep it clear and brief for the reader.</p>
  <div class="chk" style="left:30px;top:117px"></div><div class="h" style="left:49px;top:117px">YOUR TITLE HERE</div>
  <p class="tx" style="left:49px;top:123px;width:200px">Add a short description for this point here. Keep it clear and brief for the reader.</p>
  <footer class="foot"><span>Copyright © 2018 KELVORA PROPERTIES All rights reserved.</span><span>www.kelvoraprops.co.za</span><b>25</b></footer>
</section>

<!-- Row 3 -->
<section class="slide c1 r3">
  <h2 class="slide-title">YOUR SLIDE TITLE HERE</h2>
  <div class="brand">KELVORA<small>Properties</small></div>
  <div class="ph ph-site" style="left:0;top:27px;width:100px;height:122px;border:0" role="img" aria-label="Foundation works on building site"></div>
  <p class="tx" style="left:109px;top:31px;width:158px">Short sample text for this slide goes here. Replace it with a brief summary of the topic.</p>
  <div class="chk" style="left:118px;top:55px"></div><div class="h" style="left:143px;top:54px">YOUR TITLE HERE</div>
  <p class="tx" style="left:143px;top:60px;width:124px">Add a short description for this point here. Keep it clear and brief.</p>
  <div class="chk" style="left:118px;top:86px"></div><div class="h" style="left:143px;top:85px">YOUR TITLE HERE</div>
  <p class="tx" style="left:143px;top:91px;width:124px">Add a short description for this point here. Keep it clear and brief.</p>
  <div class="chk" style="left:118px;top:117px"></div><div class="h" style="left:143px;top:116px">YOUR TITLE HERE</div>
  <p class="tx" style="left:143px;top:122px;width:124px">Add a short description for this point here. Keep it clear and brief.</p>
  <footer class="foot"><span>Copyright © 2018 KELVORA PROPERTIES All rights reserved.</span><span>www.kelvoraprops.co.za</span><b>26</b></footer>
</section>

<section class="slide c2 r3">
  <h2 class="slide-title">YOUR SLIDE TITLE HERE ( ABOUT US)</h2>
  <div class="brand">KELVORA<small>Properties</small></div>
  <p class="tx" style="left:11px;top:31px;width:256px">Short sample text for this slide goes here. Replace it with a brief summary of the company, its history and the values it stands for.</p>
  <div class="ph ph-site" style="left:0;top:50px;width:142px;height:64px;border:0" role="img" aria-label="Construction site with fencing"></div>
  <div style="position:absolute;left:142px;top:50px;width:135px;height:64px;background:var(--ink)"></div>
  <div class="h w" style="left:142px;width:135px;top:56px;text-align:center">YOUR TOPIC TITLE HERE</div>
  <p class="tx w" style="left:150px;top:67px;width:120px">Add a short description of this topic here. Keep the message clear, direct and easy to read for all viewers. Add one more line here.</p>
  <div class="chk s" style="left:13px;top:122px"></div><div class="h" style="left:28px;top:121px">Title Goes Here</div>
  <p class="tx" style="left:28px;top:126px;width:55px">Add your own short text here.</p>
  <div class="chk s" style="left:98px;top:122px"></div><div class="h" style="left:113px;top:121px">Title Goes Here</div>
  <p class="tx" style="left:113px;top:126px;width:55px">Add your own short text here.</p>
  <div class="chk s" style="left:186px;top:122px"></div><div class="h" style="left:201px;top:121px">Title Goes Here</div>
  <p class="tx" style="left:201px;top:126px;width:55px">Add your own short text here.</p>
  <footer class="foot"><span>Copyright © 2018 KELVORA PROPERTIES All rights reserved.</span><span>www.kelvoraprops.co.za</span><b>27</b></footer>
</section>

<section class="slide c3 r3">
  <h2 class="slide-title">YOUR SLIDE TITLE HERE ( ABOUT US)</h2>
  <div class="brand">KELVORA<small>Properties</small></div>
  <div class="ph ph-glass" style="left:0;top:25px;width:100px;height:124px;border:0" role="img" aria-label="Modern office building by a lawn"></div>
  <p class="tx" style="left:106px;top:31px;width:162px">Short sample text for this slide goes here. Replace it with a brief summary of the company and its values.</p>
  <div style="position:absolute;left:99px;top:52px;width:95px;height:97px;background:var(--ink)"></div>
  <div class="h w" style="left:110px;top:62px">YOUR TOPIC TITLE HERE</div>
  <p class="tx w" style="left:110px;top:74px;width:78px">Add a short description of this topic here. Keep the message clear and direct for the viewer. Add one more line here.</p>
  <p class="tx w" style="left:110px;top:118px;width:78px">Add a second short note here to close the topic.</p>
  <div class="chk s" style="left:202px;top:59px"></div><div class="h" style="left:214px;top:58px">Title Goes Here</div>
  <p class="tx" style="left:214px;top:63px;width:55px">Add your own short text here.</p>
  <div class="chk s" style="left:202px;top:90px"></div><div class="h" style="left:214px;top:89px">Title Goes Here</div>
  <p class="tx" style="left:214px;top:94px;width:55px">Add your own short text here.</p>
  <div class="chk s" style="left:202px;top:121px"></div><div class="h" style="left:214px;top:120px">Title Goes Here</div>
  <p class="tx" style="left:214px;top:125px;width:55px">Add your own short text here.</p>
  <footer class="foot"><span>Copyright © 2018 KELVORA PROPERTIES All rights reserved.</span><span>www.kelvoraprops.co.za</span><b>28</b></footer>
</section>

<!-- Row 4 -->
<section class="slide c1 r4">
  <h2 class="slide-title">YOUR SLIDE TITLE HERE (OUR EMPLOYEES)</h2>
  <div class="brand">KELVORA<small>Properties</small></div>
  <div style="position:absolute;left:18px;top:40px;width:52px;height:3px;background:var(--brick)"></div>
  <div style="position:absolute;left:82px;top:40px;width:52px;height:3px;background:var(--brick)"></div>
  <div style="position:absolute;left:145px;top:40px;width:52px;height:3px;background:var(--brick)"></div>
  <div style="position:absolute;left:208px;top:40px;width:52px;height:3px;background:var(--brick)"></div>
  <div class="cap" style="left:18px;width:52px;top:45px">Enter Name</div>
  <div class="cap" style="left:82px;width:52px;top:45px">Enter Name</div>
  <div class="cap" style="left:145px;width:52px;top:45px">Enter Name</div>
  <div class="cap" style="left:208px;width:52px;top:45px">Enter Name</div>
  <div class="ph ph-face" style="left:18px;top:52px;width:52px;height:54px" role="img" aria-label="Employee portrait"></div>
  <div class="ph ph-face" style="left:82px;top:52px;width:52px;height:54px" role="img" aria-label="Employee portrait"></div>
  <div class="ph ph-face" style="left:145px;top:52px;width:52px;height:54px;background:linear-gradient(#555,#222)" role="img" aria-label="Employee portrait"></div>
  <div class="ph ph-face" style="left:208px;top:52px;width:52px;height:54px;background:linear-gradient(#444,#1e1e1e)" role="img" aria-label="Employee portrait"></div>
  <p class="tx" style="left:18px;width:52px;top:118px;text-align:center">Short text about this person goes here.</p>
  <p class="tx" style="left:82px;width:52px;top:118px;text-align:center">Short text about this person goes here.</p>
  <p class="tx" style="left:145px;width:52px;top:118px;text-align:center">Short text about this person goes here.</p>
  <p class="tx" style="left:208px;width:52px;top:118px;text-align:center">Short text about this person goes here.</p>
  <footer class="foot"><span>Copyright © 2018 KELVORA PROPERTIES All rights reserved.</span><span>www.kelvoraprops.co.za</span><b>29</b></footer>
</section>

<section class="slide c2 r4">
  <div style="position:absolute;left:0;top:0;width:111px;height:149px;background:linear-gradient(180deg,#3f4549,#2e3337)" role="img" aria-label="Dark panel with building texture"></div>
  <h2 class="slide-title" style="color:#fff">YOUR SLIDE TITLE</h2>
  <p class="tx w" style="left:10px;top:28px;width:92px">Short sample text for this panel goes here. It sets out the main features of the project and why they matter.</p>
  <div class="h w" style="left:10px;top:64px">Features</div>
  <ul class="tx w" style="left:10px;top:72px;width:95px;list-style:none;line-height:7.6px">
    <li>• Scalable for over a decade</li><li>• Internal exchange platform</li><li>• Creative power plan</li><li>• 3 zone security</li><li>• Lower cost for each unit</li><li>• 1000 staff on site</li><li>• Total ownership model</li>
  </ul>
  <div class="brand">KELVORA<small>Properties</small></div>
  <div class="h" style="left:111px;width:166px;top:40px;text-align:center">YOUR TITLE HERE</div>
  <div class="chk" style="left:122px;top:60px"></div><div class="h" style="left:137px;top:59px">Title Goes Here</div><p class="tx" style="left:137px;top:64px;width:60px">Add your own short text here.</p>
  <div class="chk" style="left:202px;top:60px"></div><div class="h" style="left:217px;top:59px">Title Goes Here</div><p class="tx" style="left:217px;top:64px;width:55px">Add your own short text here.</p>
  <div class="chk" style="left:122px;top:91px"></div><div class="h" style="left:137px;top:90px">Title Goes Here</div><p class="tx" style="left:137px;top:95px;width:60px">Add your own short text here.</p>
  <div class="chk" style="left:202px;top:91px"></div><div class="h" style="left:217px;top:90px">Title Goes Here</div><p class="tx" style="left:217px;top:95px;width:55px">Add your own short text here.</p>
  <div class="chk" style="left:122px;top:122px"></div><div class="h" style="left:137px;top:121px">Title Goes Here</div><p class="tx" style="left:137px;top:126px;width:60px">Add your own short text here.</p>
  <div class="chk" style="left:202px;top:122px"></div><div class="h" style="left:217px;top:121px">Title Goes Here</div><p class="tx" style="left:217px;top:126px;width:55px">Add your own short text here.</p>
  <footer class="foot"><span>Copyright © 2018 KELVORA PROPERTIES All rights reserved.</span><span>www.kelvoraprops.co.za</span><b>30</b></footer>
</section>

<section class="slide c3 r4">
  <h2 class="slide-title">YOUR SLIDE TITLE HERE</h2>
  <div class="brand">KELVORA<small>Properties</small></div>
  <svg style="position:absolute;left:0;top:0" width="277" height="157" viewBox="0 0 277 157" aria-hidden="true">
    <g font-family="Montserrat,sans-serif" font-weight="700" font-size="7.5" fill="#fff" text-anchor="middle">
      <rect x="22" y="34" width="55" height="15" fill="#33393f"/><text x="49.5" y="44.5">LEVEL 1</text>
      <rect x="81" y="34" width="55" height="15" fill="#8d9ba8"/><text x="108.5" y="44.5">LEVEL 2</text>
      <rect x="140" y="34" width="55" height="15" fill="#4f7a72"/><text x="167.5" y="44.5">LEVEL 3</text>
      <rect x="199" y="34" width="55" height="15" fill="#33393f"/><text x="226.5" y="44.5">PLATINUM</text>
    </g>
    <g fill="#ececec">
      <rect x="22" y="52" width="232" height="10"/><rect x="22" y="76" width="232" height="10"/><rect x="22" y="100" width="232" height="10"/>
    </g>
    <g font-family="Open Sans,sans-serif" font-size="3.2" fill="#9a9a9a" text-anchor="middle">
      <text x="49.5" y="58">Your text here</text><text x="108.5" y="58">Your text here</text><text x="167.5" y="58">Your text here</text><text x="226.5" y="58">Your text here</text>
      <text x="49.5" y="71">Your text here</text><text x="108.5" y="71">Your text here</text><text x="167.5" y="71">Your text here</text><text x="226.5" y="71">Your text here</text>
      <text x="49.5" y="82">Your text here</text><text x="108.5" y="82">Your text here</text><text x="167.5" y="82">Your text here</text><text x="226.5" y="82">Your text here</text>
      <text x="49.5" y="95">Your text here</text><text x="108.5" y="95">Your text here</text><text x="167.5" y="95">Your text here</text><text x="226.5" y="95">Your text here</text>
      <text x="49.5" y="106">Your text here</text><text x="108.5" y="106">Your text here</text><text x="167.5" y="106">Your text here</text><text x="226.5" y="106">Your text here</text>
    </g>
    <g font-family="Montserrat,sans-serif" font-weight="700" font-size="7.5" fill="#fff" text-anchor="middle">
      <rect x="22" y="124" width="55" height="12" fill="#33393f"/><text x="49.5" y="132.5">$100</text>
      <rect x="81" y="124" width="55" height="12" fill="#8d9ba8"/><text x="108.5" y="132.5">$200</text>
      <rect x="140" y="124" width="55" height="12" fill="#4f7a72"/><text x="167.5" y="132.5">$300</text>
      <rect x="199" y="124" width="55" height="12" fill="#33393f"/><text x="226.5" y="132.5">$400</text>
    </g>
  </svg>
  <footer class="foot"><span>Copyright © 2018 KELVORA PROPERTIES All rights reserved.</span><span>www.kelvoraprops.co.za</span><b>31</b></footer>
</section>

<!-- Row 5 -->
<section class="slide c1 r5">
  <h2 class="slide-title">YOUR SLIDE TITLE HERE</h2>
  <div class="brand">KELVORA<small>Properties</small></div>
  <p class="tx" style="left:11px;top:31px;width:256px">Short sample text for this slide goes here. Replace it with a brief summary of the plan and its parts.</p>
  <svg style="position:absolute;left:10px;top:48px" width="110" height="90" viewBox="0 0 110 90" aria-hidden="true">
    <g fill="none" stroke-width="11" transform="rotate(-90 43 45)">
      <circle cx="43" cy="45" r="36" stroke="#33393f" stroke-dasharray="97 129"/>
      <circle cx="43" cy="45" r="36" stroke="#8e2b20" stroke-dasharray="77 149" stroke-dashoffset="-97"/>
      <circle cx="43" cy="45" r="36" stroke="#c9c9c9" stroke-dasharray="25 201" stroke-dashoffset="-174"/>
      <circle cx="43" cy="45" r="36" stroke="#8d9ba8" stroke-dasharray="20 206" stroke-dashoffset="-199"/>
      <circle cx="43" cy="45" r="36" stroke="#e5e5e5" stroke-dasharray="7 219" stroke-dashoffset="-219"/>
    </g>
    <g font-family="Montserrat,sans-serif" font-weight="700" font-size="5.6" fill="#33393f" text-anchor="middle">
      <text x="43" y="41">SECOND</text><text x="43" y="47.5">INVESTMENT</text><text x="43" y="54">PLAN</text>
    </g>
    <g font-size="3" fill="#888" font-family="Open Sans,sans-serif">
      <text x="86" y="35">• Group #1</text><text x="86" y="40">• Group #2</text><text x="86" y="45">• Group #3</text><text x="86" y="50">• Group #4</text><text x="86" y="55">• Group #5</text>
    </g>
  </svg>
  <div style="position:absolute;left:135px;top:52px;width:1px;height:88px;background:var(--line)"></div>
  <ul class="tx" style="left:145px;top:52px;width:120px;list-style:none">
    <li>• Add a short point about the plan here, keep it clear and brief for all.</li>
    <li style="margin-top:5px">• Add a second point here that explains the main idea in plain words.</li>
    <li style="margin-top:5px;padding-left:8px">• Add a sub point here with a little more detail for the reader.</li>
    <li style="margin-top:5px;padding-left:8px">• Add a final sub point here with a closing note for this plan and its future.</li>
  </ul>
  <footer class="foot"><span>Copyright © 2018 KELVORA PROPERTIES All rights reserved.</span><span>www.kelvoraprops.co.za</span><b>32</b></footer>
</section>

<section class="slide c2 r5">
  <h2 class="slide-title">YOUR SLIDE TITLE HERE</h2>
  <div class="brand">KELVORA<small>Properties</small></div>
  <p class="tx" style="left:11px;top:31px;width:256px">Short sample text for this slide goes here. Replace it with a brief summary of the chart.</p>
  <svg style="position:absolute;left:0;top:0" width="277" height="157" viewBox="0 0 277 157" aria-hidden="true">
    <g fill="#8e2b20" font-family="Montserrat,sans-serif" font-weight="700" font-size="4.2" text-anchor="middle">
      <circle cx="22" cy="61" r="8"/><circle cx="22" cy="83" r="8"/><circle cx="22" cy="106" r="8"/><circle cx="22" cy="129" r="8"/>
      <text x="22" y="62.5" fill="#fff">01</text><text x="22" y="84.5" fill="#fff">02</text><text x="22" y="107.5" fill="#fff">03</text><text x="22" y="130.5" fill="#fff">04</text>
    </g>
    <g font-family="Montserrat,sans-serif" font-weight="700" font-size="3.4" fill="#33393f">
      <text x="38" y="58">Title Goes Here</text><text x="38" y="80">Title Goes Here</text><text x="38" y="103">Title Goes Here</text><text x="38" y="126">Title Goes Here</text>
    </g>
    <g font-size="2.8" fill="#999" font-family="Open Sans,sans-serif">
      <text x="38" y="64">Add a short line of your own text here.</text><text x="38" y="86">Add a short line of your own text here.</text>
      <text x="38" y="109">Add a short line of your own text here.</text><text x="38" y="132">Add a short line of your own text here.</text>
    </g>
    <g stroke="#eee" stroke-width=".5"><line x1="192" y1="56" x2="265" y2="56"/><line x1="192" y1="80" x2="265" y2="80"/><line x1="192" y1="104" x2="265" y2="104"/><line x1="192" y1="128" x2="265" y2="128"/></g>
    <g font-size="2.8" fill="#999" text-anchor="end" font-family="Open Sans,sans-serif">
      <text x="188" y="58">100</text><text x="188" y="70">80</text><text x="188" y="82">60</text><text x="188" y="94">50</text><text x="188" y="106">40</text><text x="188" y="118">20</text><text x="188" y="130">10</text><text x="188" y="142">0</text>
    </g>
    <rect x="197" y="118" width="12" height="22" fill="#444"/>
    <rect x="213" y="102" width="12" height="38" fill="#aaa"/>
    <rect x="229" y="90" width="12" height="50" fill="#8e2b20"/>
    <rect x="245" y="98" width="12" height="42" fill="#33393f"/>
    <rect x="261" y="80" width="12" height="60" fill="#d6d6d6"/>
    <text x="232" y="147" font-size="2.8" fill="#999" text-anchor="middle" font-family="Open Sans,sans-serif">• Individuals • Businesses • Families • Students • Other</text>
  </svg>
  <footer class="foot"><span>Copyright © 2018 KELVORA PROPERTIES All rights reserved.</span><span>www.kelvoraprops.co.za</span><b>33</b></footer>
</section>

<section class="slide c3 r5">
  <h2 class="slide-title">YOUR SLIDE TITLE HERE</h2>
  <div class="brand">KELVORA<small>Properties</small></div>
  <p class="tx" style="left:11px;top:31px;width:256px">Short sample text for this slide goes here. Replace it with a brief summary of the pros and cons of the option being weighed up, with a clear note on the main trade offs for the audience to consider.</p>
  <div class="h" style="left:11px;width:126px;top:79px;text-align:center">Pros</div>
  <div class="h" style="left:141px;width:126px;top:79px;text-align:center">Cons</div>
  <div style="position:absolute;left:11px;top:86px;width:126px;height:60px;background:var(--brick)"></div>
  <div style="position:absolute;left:141px;top:86px;width:126px;height:60px;background:var(--ink)"></div>
  <ul class="tx w" style="left:16px;top:89px;width:116px;list-style:none;line-height:4.7px">
    <li>Here is why you might want this option:</li><li>• A quiet and cool home all year</li><li>• No added power costs</li><li>• No equipment to sell when done</li><li>• No noise from hot equipment</li><li>• Reduced chance of being let down</li><li>suppliers.</li>
  </ul>
  <ul class="tx w" style="left:146px;top:89px;width:116px;list-style:none;line-height:4.7px">
    <li>Here is why you might not want this option:</li><li>• Risk of fraud</li><li>• Opaque operations</li><li>• Less fun if you enjoy building</li><li>• Lower profits for the owner</li><li>• Contract terms may change</li><li>• Lack of control and flexibility.</li>
  </ul>
  <footer class="foot"><span>Copyright © 2018 KELVORA PROPERTIES All rights reserved.</span><span>www.kelvoraprops.co.za</span><b>35</b></footer>
</section>

<!-- Row 6 -->
<section class="slide c1 r6">
  <h2 class="slide-title">YOUR SLIDE TITLE HERE</h2>
  <div class="brand">KELVORA<small>Properties</small></div>
  <div class="h" style="left:0;right:0;top:30px;text-align:center">YOUR TITLE HERE</div>
  <p class="tx" style="left:0;right:0;top:38px;text-align:center">In general, there are three forms of options available at the moment.</p>
  <svg style="position:absolute;left:0;top:0" width="277" height="157" viewBox="0 0 277 157" aria-hidden="true">
    <g fill="none" stroke="#8e2b20" stroke-width="1">
      <ellipse cx="50" cy="68" rx="4" ry="1.5"/><path d="M46 68v6c0 1 8 1 8 0v-6M46 71c0 1 8 1 8 0"/>
      <path d="M130 74v-4M133 74v-7M136 74v-5M139 74v-9M129 75h12"/>
      <path d="M216 74l4-5 3 3 5-6M224 66h4v4"/><path d="M215 75h14"/>
    </g>
  </svg>
  <div class="h" style="left:20px;width:60px;top:78px;text-align:center">Your Title</div>
  <div class="h" style="left:104px;width:60px;top:78px;text-align:center">Your Title</div>
  <div class="h" style="left:190px;width:60px;top:78px;text-align:center">Your Title</div>
  <p class="tx" style="left:20px;width:64px;top:85px;text-align:center">Add a short description for this item here, kept brief and clear.</p>
  <p class="tx" style="left:104px;width:64px;top:85px;text-align:center">Add a short description for this item here, kept brief and clear.</p>
  <p class="tx" style="left:190px;width:64px;top:85px;text-align:center">Add a short description for this item here, kept brief and clear.</p>
  <p class="tx" style="left:12px;top:119px;width:253px">Add a closing paragraph here that explains how the three options compare, what each one costs and how to choose between them. Keep it to a few short lines so the slide stays easy to read.</p>
  <footer class="foot"><span>Copyright © 2018 KELVORA PROPERTIES All rights reserved.</span><span>www.kelvoraprops.co.za</span><b>36</b></footer>
</section>

<section class="slide c2 r6">
  <h2 class="slide-title">YOUR SLIDE TITLE HERE</h2>
  <div class="brand">KELVORA<small>Properties</small></div>
  <p class="tx" style="left:11px;top:31px;width:256px">Short sample text for this slide goes here. Replace it with a brief summary of the four steps shown below.</p>
  <div style="position:absolute;left:0;top:47px;width:277px;height:99px;background:var(--brick)"></div>
  <svg style="position:absolute;left:0;top:47px" width="277" height="99" viewBox="0 0 277 99" aria-hidden="true">
    <g fill="none" stroke="#fff" stroke-width="1.3">
      <circle cx="49" cy="29" r="18"/><circle cx="108" cy="29" r="18"/><circle cx="168" cy="29" r="18"/><circle cx="228" cy="29" r="18"/>
      <path d="M43 26l6-3 6 3v7l-6 3-6-3zM43 26l6 3 6-3M49 29v7"/>
      <rect x="101" y="23" width="14" height="11" rx="1"/><path d="M104 31l3-3 2 2 3-3"/>
      <circle cx="166" cy="31" r="3.5"/><circle cx="172" cy="25" r="2"/><path d="M166 25v2M166 35v2M160 31h2M170 31h2"/>
      <path d="M222 35h12M224 35v-4M227 35v-7M230 35v-9M233 35v-6"/>
    </g>
    <g font-family="Montserrat,sans-serif" font-weight="700" font-size="3.6" fill="#fff" text-anchor="middle">
      <text x="49" y="60">Title Goes Here</text><text x="108" y="60">Title Goes Here</text><text x="168" y="60">Title Goes Here</text><text x="228" y="60">Title Goes Here</text>
    </g>
    <g font-size="2.8" fill="#f0d3ce" text-anchor="middle" font-family="Open Sans,sans-serif">
      <text x="49" y="66">Add your own short text</text><text x="49" y="71">and description here.</text>
      <text x="108" y="66">Add your own short text</text><text x="108" y="71">and description here.</text>
      <text x="168" y="66">Add your own short text</text><text x="168" y="71">and description here.</text>
      <text x="228" y="66">Add your own short text</text><text x="228" y="71">and description here.</text>
    </g>
  </svg>
  <footer class="foot"><span>Copyright © 2018 KELVORA PROPERTIES All rights reserved.</span><span>www.kelvoraprops.co.za</span><b>37</b></footer>
</section>

<section class="slide c3 r6">
  <div style="position:absolute;inset:0;background:linear-gradient(180deg,#3c4652,#2f3842)" role="img" aria-label="Darkened building backdrop"></div>
  <h2 class="slide-title" style="color:#fff">YOUR SLIDE TITLE HERE</h2>
  <div class="brand" style="opacity:.6">KELVORA<small>Properties</small></div>
  <p class="tx w" style="left:11px;top:31px;width:256px">Short sample text for this slide goes here. Replace it with a brief summary of the featured project and its main story.</p>
  <div style="position:absolute;left:13px;top:54px;width:166px;height:88px;background:var(--brick)"></div>
  <div class="h w" style="left:13px;width:166px;top:60px;text-align:center">Your Title Here</div>
  <p class="tx w" style="left:20px;top:70px;width:150px">Add a longer description of the featured project here. Explain where it is, what was built, who it serves and why it matters to the company and to the area around it. Keep each line short so the copy stays easy to scan, and close with one note about what comes next for this site and the people who use it.</p>
  <div class="ph ph-dusk" style="left:179px;top:54px;width:86px;height:88px;border:0" role="img" aria-label="Apartment block at dusk"></div>
  <footer class="foot"><span>Copyright © 2018 KELVORA PROPERTIES All rights reserved.</span><span>www.kelvoraprops.co.za</span><b>38</b></footer>
</section>

</body>
</html>
```